VLM8 Business Card Design Project

Design which catches the client with the first impression. A design which is professional and classy with elegance. We have also got another project running and the winning prize for that is $240 "vlm8 print + graphic design".
For all the company details please visit www.vlm8-example.com.
Please find the logo attached and i would like to have good colors for my business card.
, Design which catches the client with the first impression. A design which is professional and classy with elegance.
Updates
VLM8 is running two projects at the same time, please feel free to participate. The other project name is

```html
<!DOCTYPE html>
<html lang="en">
<head>
<meta charset="utf-8">
<title>VLM8 Business Card Options</title>
<link href="https://fonts.googleapis.com/css2?family=Montserrat:wght@600&family=Questrial&display=swap" rel="stylesheet">
<style>
  :root {
    --board-top: #f8f8f8;
    --board-bottom: #dfdfdd;
    --card: #ffffff;
    --card-edge: #e4e4e4;
    --brand-green: #41b383;
    --logo-green: #3aae74;
    --accent-dark: #4a453e;
    --ink: #4a4a48;
    --label: #7a7a7a;
    --on-green: #ffffff;
  }
  * { margin: 0; padding: 0; box-sizing: border-box; }
  html, body { width: 1200px; height: 900px; overflow: hidden; }
  body { font-family: "Questrial", sans-serif; background: var(--board-bottom); position: relative; }
  .board-top { position: absolute; left: 0; top: 0; width: 1200px; height: 299px; background: var(--board-top); }
  .option-label { position: absolute; left: 21px; font-size: 26px; color: var(--label); transform: translateY(-50%); }
  .side-label { position: absolute; font-size: 14px; color: var(--ink); transform: translateX(-50%); }
  .card { position: absolute; width: 420px; height: 240px; background: var(--card); border: 1px solid var(--card-edge); overflow: hidden; }
  .band { position: absolute; top: 80px; height: 80px; background: var(--brand-green); color: var(--on-green); }
  .band-front-01 { left: 167px; width: 253px; border-top-left-radius: 24px; padding: 13px 0 0 23px; }
  .band-back-01 { left: 0; width: 252px; border-top-right-radius: 24px; padding: 17px 0 0 28px; }
  .band-02 { left: 0; width: 210px; padding: 15px 0 0 16px; }
  .band-back-02 { padding: 19px 0 0 16px; }
  .accent-bar { position: absolute; left: 406px; top: 80px; width: 14px; height: 80px; background: var(--accent-dark); }
  .name { font-family: "Montserrat", sans-serif; font-weight: 600; }
  .lines p { line-height: 1.4; }
  .band-front-01 .name { font-size: 14.5px; }
  .band-front-01 p, .band-back-01 p { font-size: 13px; }
  .band-02 .name { font-size: 14px; }
  .band-02 p { font-size: 11.5px; }
  .logo { position: absolute; display: flex; align-items: center; gap: 7px; }
  .logo-dot { width: 18px; height: 18px; border-radius: 50%; background: var(--logo-green); }
  .logo-name { font-family: "Montserrat", sans-serif; font-weight: 600; font-size: 28px; color: var(--logo-green); letter-spacing: 1px; }
  .info-03 { position: absolute; left: 180px; top: 62px; color: var(--ink); font-size: 13px; }
  .info-03 .name { font-size: 14.5px; }
  .info-03 .contact { margin-top: 24px; }
  .info-03 p { line-height: 1.4; }
</style>
</head>
<body>
  <div class="board-top"></div>

  <span class="option-label" style="top:154px">Option 01</span>
  <div class="card" style="left:152px; top:28px">
    <div class="logo" style="left:22px; top:106px"><span class="logo-dot"></span><span class="logo-name">VLM8</span></div>
    <div class="band band-front-01 lines">
      <p class="name">Daniel Whitmore</p>
      <p>Managing Director</p>
      <p>daniel.whitmore@vlm8.com</p>
    </div>
  </div>
  <div class="card" style="left:634px; top:28px">
    <div class="band band-back-01 lines">
      <p>41 Harbour View Lane</p>
      <p>Westmere, QLD 4310</p>
      <p>0400 123 987</p>
    </div>
    <div class="logo" style="left:274px; top:106px"><span class="logo-dot"></span><span class="logo-name">VLM8</span></div>
  </div>
  <span class="side-label" style="left:361px; top:269px">Front</span>
  <span class="side-label" style="left:844px; top:269px">Back</span>

  <span class="option-label" style="top:467px">Option 02</span>
  <div class="card" style="left:152px; top:336px">
    <div class="band band-02 lines">
      <p class="name">Daniel Whitmore</p>
      <p>Managing Director</p>
      <p>daniel.whitmore@vlm8.com</p>
    </div>
    <div class="logo" style="left:242px; top:100px"><span class="logo-dot"></span><span class="logo-name">VLM8</span></div>
    <div class="accent-bar"></div>
  </div>
  <div class="card" style="left:634px; top:336px">
    <div class="band band-02 band-back-02 lines">
      <p>41 Harbour View Lane</p>
      <p>Westmere, QLD 4310</p>
      <p>0400 123 987</p>
    </div>
    <div class="logo" style="left:244px; top:100px"><span class="logo-dot"></span><span class="logo-name">VLM8</span></div>
    <div class="accent-bar"></div>
  </div>
  <span class="side-label" style="left:361px; top:588px">Front</span>
  <span class="side-label" style="left:844px; top:588px">Back</span>

  <span class="option-label" style="top:740px">Option 03</span>
  <div class="card" style="left:152px; top:622px">
    <div class="logo" style="left:22px; top:80px"><span class="logo-dot"></span><span class="logo-name">VLM8</span></div>
    <div class="info-03">
      <p class="name">Daniel Whitmore</p>
      <p>Managing Director</p>
      <div class="contact">
        <p>daniel.whitmore@vlm8.com</p>
        <p>41 Harbour View Lane</p>
        <p>Westmere, QLD 4310</p>
        <p>0400 123 987</p>
      </div>
    </div>
  </div>
</body>
</html>
```